Inspiration Poster

Inspirational Poster that has a Dorin Velk like abstract look (http://www.quorvix.com/images/search?q=dorin+velk&FORM=HDRSC2) with the text:

"we walk not in order to arrive at the promise land but because walking itself is a revolution"
-Mark Fennimore

```html
<!DOCTYPE html>
<html lang="en">
<head>
<meta charset="utf-8">
<title>We Walk – Mark Fennimore</title>
<link rel="stylesheet" href="https://fonts.googleapis.com/css2?family=Poiret+One&display=swap">
<style>
  :root {
    --ink-yellow: #f2e600;
    --street-light: #b9b9b9;
    --street-mid: #6f6f6f;
    --street-dark: #2a2a2a;
    --panel-shade: rgba(20, 20, 20, 0.55);
    --label-shade: rgba(90, 90, 90, 0.85);
  }
  html, body {
    margin: 0;
    padding: 0;
    width: 847px;
    height: 1200px;
    overflow: hidden;
    background: #ffffff;
  }
  .poster {
    position: relative;
    width: 847px;
    height: 1200px;
    overflow: hidden;
    font-family: "Poiret One", sans-serif;
    color: var(--ink-yellow);
  }
  .street-photo {
    position: absolute;
    inset: 0;
    background: linear-gradient(135deg, var(--street-light) 0%, var(--street-mid) 45%, var(--street-dark) 70%, var(--street-mid) 100%);
  }
  .quote-panel {
    position: absolute;
    left: 150px;
    top: 105px;
    width: 578px;
    height: 938px;
    background: var(--panel-shade);
  }
  .frame {
    position: absolute;
    inset: 0;
  }
  .quote {
    position: absolute;
    left: 150px;
    width: 578px;
    top: 0;
    height: 1200px;
    text-transform: uppercase;
  }
  .line {
    position: absolute;
    left: 0;
    right: 0;
    text-align: center;
    line-height: 1;
    white-space: nowrap;
    font-weight: 400;
  }
  .line-small { font-size: 56px; letter-spacing: 1px; }
  .line-large { font-size: 108px; letter-spacing: 2px; }
  .we-walk { top: 168px; }
  .not { top: 215px; font-size: 96px; }
  .in-order-to { top: 300px; }
  .in-order-to .in { position: absolute; left: 92px; top: 0; }
  .in-order-to .order { position: absolute; left: 205px; top: 18px; }
  .in-order-to .to { position: absolute; left: 390px; top: -6px; }
  .arrive { top: 360px; }
  .at-the { top: 500px; }
  .promise-land { top: 560px; }
  .but-because { top: 628px; }
  .walking { top: 705px; font-size: 112px; }
  .itself { top: 810px; }
  .revolution { top: 870px; font-size: 106px; }
  .author {
    position: absolute;
    left: 243px;
    top: 1088px;
    width: 359px;
    height: 62px;
    background: var(--label-shade);
    display: flex;
    align-items: center;
    justify-content: center;
    font-size: 30px;
    letter-spacing: 2px;
    text-transform: uppercase;
  }
  .author-rule {
    position: absolute;
    left: 14px;
    right: 14px;
    height: 0;
    border-top: 1.5px solid var(--ink-yellow);
  }
  .author-rule.top { top: 8px; }
  .author-rule.bottom { bottom: 8px; }
</style>
</head>
<body>
<main class="poster">
  <div class="street-photo" role="img" aria-label="Black and white overhead photograph of people crossing a striped pedestrian crosswalk"></div>
  <div class="quote-panel"></div>

  <svg class="frame" width="847" height="1200" viewBox="0 0 847 1200" fill="none" stroke="var(--ink-yellow)" stroke-width="2">
    <rect x="132" y="94" width="606" height="944"/>
    <rect x="142" y="104" width="586" height="924"/>
    <line x1="190" y1="1028" x2="690" y2="1028"/>
    <g class="corner-rings">
      <circle cx="108" cy="90" r="33"/><circle cx="108" cy="90" r="27"/>
      <circle cx="758" cy="90" r="33"/><circle cx="758" cy="90" r="27"/>
      <circle cx="108" cy="1008" r="33"/><circle cx="108" cy="1008" r="27"/>
      <circle cx="732" cy="1008" r="33"/><circle cx="732" cy="1008" r="27"/>
    </g>
  </svg>

  <section class="quote">
    <div class="line line-small we-walk">We Walk</div>
    <div class="line line-large not">Not</div>
    <div class="line line-small in-order-to"><span class="in">In</span><span class="order">Order</span><span class="to">To</span></div>
    <div class="line line-large arrive">Arrive</div>
    <div class="line line-small at-the">At the</div>
    <div class="line line-small promise-land">Promise Land</div>
    <div class="line line-small but-because">But Because</div>
    <div class="line line-large walking">Walking</div>
    <div class="line line-small itself">Itself is a</div>
    <div class="line line-large revolution">Revolution</div>
  </section>

  <div class="author">
    <span class="author-rule top"></span>
    Mark Fennimore
    <span class="author-rule bottom"></span>
  </div>
</main>
</body>
</html>
```